Global social media analytics company needs business card design

We need an updated business card design to align with our new website - brightquillo.net -

I would also like a favicon designed as well.

Target Market(s)

CEOs, CMOs go big companies

Industry/Entity Type

Business

Contact Information for Business Card

Room for the following:
Address
Main telephone
Direct telephone or cell phone
twitter handle

Colors
aaaaaa

Requirements
Must have
• Attention to detail; style.
• Use the logo color from our website - which is gray

```html
<!DOCTYPE html>
<html lang="en">
<head>
<meta charset="utf-8">
<title>Brightquillo Stationery</title>
<link rel="stylesheet" href="https://fonts.googleapis.com/css2?family=Lato:wght@400;700;900&family=Arimo:wght@400&display=swap">
<style>
:root{
  --bg:#efefef;
  --paper:#ffffff;
  --ink:#3f4141;
  --text:#444646;
  --muted:#6a6c6c;
  --faint:#ebebeb;
  --sign:#1d3a8f;
}
*{margin:0;padding:0;box-sizing:border-box}
html,body{width:1200px;height:815px;overflow:hidden;background:var(--bg)}
body{position:relative;font-family:'Lato',sans-serif;color:var(--text)}
.sheet{position:absolute;background:var(--paper);box-shadow:0 3px 6px rgba(0,0,0,.28);overflow:hidden}
.brand{position:absolute;display:flex;flex-direction:column;align-items:center}
.brand-dot{border-radius:50%;background:var(--ink)}
.brand-name{font-family:'Lato',sans-serif;font-weight:900;color:var(--ink);letter-spacing:-.3px;line-height:1}
.abs{position:absolute}
.contact-row{display:flex;align-items:center;gap:5px}
.contact-row svg{flex:none}

/* letterhead */
.letterhead{left:66px;top:53px;width:523px;height:733px}
.letterhead .brand{left:48px;top:32px}
.letterhead .brand-dot{width:66px;height:66px}
.letterhead .brand-name{font-size:22px;margin-top:12px}
.lh-company{left:356px;top:32px;font-size:10px;line-height:13px;color:var(--muted)}
.lh-company strong{display:block;font-size:11px;color:var(--text);margin-bottom:1px}
.lh-company .contacts{margin-top:10px;display:flex;flex-direction:column;gap:1px}
.recipient{left:49px;top:208px;font-family:'Arimo',sans-serif;font-size:8.6px;line-height:10px;color:var(--text)}
.letter-body{left:49px;top:262px;width:416px;font-family:'Arimo',sans-serif;font-size:8.3px;line-height:10.4px;color:var(--text)}
.letter-body p{margin-bottom:11px}
.letter-body p.gap{margin-top:10px}
.signature{left:49px;top:468px;width:100px;height:58px;background:linear-gradient(90deg,rgba(29,58,143,.18),rgba(29,58,143,.05));border-radius:4px}
.signer{left:49px;top:536px;font-family:'Arimo',sans-serif;font-size:9px;line-height:11px}
.watermark-disc{left:274px;top:472px;width:232px;height:232px;border-radius:50%;background:var(--faint)}
.footer-band{position:absolute;left:0;bottom:0;width:100%}

/* cards */
.card-front{left:741px;top:53px;width:262px;height:155px;background:var(--ink)}
.card-front .brand{left:0;width:100%;top:27px}
.card-front .brand-dot{width:68px;height:68px;background:#fff}
.card-front .brand-name{color:#fff;font-size:22px;margin-top:14px}
.card-back{left:741px;top:227px;width:262px;height:155px}
.card-back .brand{left:32px;top:34px}
.card-back .brand-dot{width:44px;height:44px}
.card-back .brand-name{font-size:14px;margin-top:8px}
.card-info{left:146px;top:19px;font-size:7px;line-height:10px;color:var(--muted)}
.card-info .person{font-size:10.5px;font-weight:700;color:var(--text);line-height:12px}
.card-info .role{font-size:7.5px;margin-bottom:9px}
.card-info .contacts{display:flex;flex-direction:column;gap:2px;margin-bottom:9px}
.card-info .company{font-weight:700;color:var(--text);font-size:7.5px}

/* envelopes */
.envelope-front{left:659px;top:400px;width:426px;height:184px}
.envelope-front .brand{left:31px;top:13px;align-items:flex-start}
.envelope-front .brand-dot{width:48px;height:48px;margin-left:18px}
.envelope-front .brand-name{font-size:15px;margin-top:9px}
.env-address{left:32px;top:88px;font-size:6.8px;line-height:10px;color:var(--muted);text-align:center}
.envelope-back{left:659px;top:598px;width:426px;height:187px}
.envelope-back svg{position:absolute;left:0;top:0}
</style>
</head>
<body>

<!-- Letterhead -->
<section class="sheet letterhead">
  <div class="brand">
    <div class="brand-dot"></div>
    <div class="brand-name">brightquillo</div>
  </div>
  <div class="abs lh-company">
    <strong>Brightquillo Inc.</strong>
    2270 Alder Park Ave. 4th Fl<br>Northfield, MA 01360
    <div class="contacts">
      <div class="contact-row"><svg width="8" height="8" viewBox="0 0 8 8"><path d="M1.5 .5l1.5 1.6-.8 1a4.5 4.5 0 0 0 1.9 1.9l1-.8 1.6 1.5-1 1.1C3.5 6.7 1.3 4.5.4 1.5z" fill="#555"/></svg>+1 555 014 2290</div>
      <div class="contact-row"><svg width="8" height="6" viewBox="0 0 8 6"><rect width="8" height="6" fill="#555"/><path d="M0 0l4 3 4-3" stroke="#fff" stroke-width=".8" fill="none"/></svg>info@brightquillo.net</div>
      <div class="contact-row"><svg width="8" height="8" viewBox="0 0 8 8"><circle cx="4" cy="4" r="3.6" fill="#555"/><path d="M.5 4h7M4 .4v7.2" stroke="#fff" stroke-width=".6"/></svg>www.brightquillo.net</div>
    </div>
  </div>

  <div class="abs recipient">
    Mr. Daniel Hart<br>Commercial Director<br>410 County Road 9<br>Millbrook, Mo 65000
  </div>

  <div class="abs letter-body">
    <p>Designing an effective letterhead is a unique challenge. Sometimes your letterhead design will be the first interaction a customer has had with a particular company, while other times it will be used to reinforce the brand identity. It's crucial to get the details right, but to also produce something that's tactile, eye-catching, and memorable. Designing an effective letterhead is a unique challenge. Sometimes your letterhead design will be the first interaction a customer has had with a particular company, while other times it will be used to reinforce the brand identity. It's crucial to get the details right, but to also produce something that's tactile, eye-catching, and memorable. Designing an effective letterhead is a unique challenge.</p>
    <p>Sometimes your letterhead design will be the first interaction a customer has had with a particular company, while other times it will be used to reinforce the brand identity. It's crucial to get the details right, but to also produce something that's tactile, eye-catching, and memorable. Designing an effective letterhead is a unique challenge. Sometimes your letterhead design will be the first interaction a customer has had with a particular company, while other times it will be used to reinforce the brand identity. It's crucial to get the details right, but to also produce something that's tactile, eye-catching, and memorable.</p>
    <p class="gap">Designing an effective letterhead is a unique challenge. Sometimes your letterhead design will be the first interaction a customer has had with a particular company, while other times it will be used to reinforce the brand identity. It's crucial to get the details right, but to also produce something that's tactile, eye-catching, and memorable.</p>
  </div>

  <div class="abs watermark-disc"></div>
  <div class="abs signature" role="img" aria-label="Handwritten signature of Daniel Hart"></div>
  <div class="abs signer">Daniel Hart<br>Commercial Director</div>

  <svg class="footer-band" width="523" height="32" viewBox="0 0 523 32">
    <path d="M0 12H256Q264 12 270 4Q273 0 280 0H523V32H0Z" fill="var(--ink)"/>
  </svg>
</section>

<!-- Business card front -->
<section class="sheet card-front">
  <div class="brand">
    <div class="brand-dot"></div>
    <div class="brand-name">brightquillo</div>
  </div>
</section>

<!-- Business card back -->
<section class="sheet card-back">
  <div class="brand">
    <div class="brand-dot"></div>
    <div class="brand-name">brightquillo</div>
  </div>
  <div class="abs card-info">
    <div class="person">Marcus Reed</div>
    <div class="role">President</div>
    <div class="contacts">
      <div class="contact-row"><svg width="7" height="7" viewBox="0 0 8 8"><path d="M1.5 .5l1.5 1.6-.8 1a4.5 4.5 0 0 0 1.9 1.9l1-.8 1.6 1.5-1 1.1C3.5 6.7 1.3 4.5.4 1.5z" fill="#555"/></svg>+1 555 014 2290</div>
      <div class="contact-row"><svg width="7" height="5" viewBox="0 0 8 6"><rect width="8" height="6" fill="#555"/><path d="M0 0l4 3 4-3" stroke="#fff" stroke-width=".8" fill="none"/></svg>info@brightquillo.net</div>
      <div class="contact-row"><svg width="7" height="7" viewBox="0 0 8 8"><circle cx="4" cy="4" r="3.6" fill="#555"/><path d="M.5 4h7M4 .4v7.2" stroke="#fff" stroke-width=".6"/></svg>www.brightquillo.net</div>
    </div>
    <div class="company">Brightquillo Inc.</div>
    2270 Alder Park Ave. 4th Fl<br>Northfield, MA 01360
  </div>
  <svg class="footer-band" width="262" height="16" viewBox="0 0 262 16">
    <path d="M0 6H132Q136 6 139 2Q140 0 144 0H262V16H0Z" fill="var(--ink)"/>
  </svg>
</section>

<!-- Envelope front -->
<section class="sheet envelope-front">
  <div class="brand">
    <div class="brand-dot"></div>
    <div class="brand-name">brightquillo</div>
  </div>
  <div class="abs env-address">2270 Alder Park Ave. 4th Fl<br>Northfield, MA 01360</div>
  <svg class="footer-band" width="426" height="22" viewBox="0 0 426 22">
    <path d="M0 8H232Q237 8 240 3Q242 0 247 0H426V22H0Z" fill="var(--ink)"/>
  </svg>
</section>

<!-- Envelope back -->
<section class="sheet envelope-back">
  <svg width="426" height="187" viewBox="0 0 426 187">
    <path d="M6 0V54Q6 61 14 61H412Q420 61 420 54V0" fill="#fbfbfb" stroke="#cfcfcf" stroke-width="1"/>
  </svg>
</section>

</body>
</html>
```